Bref créative
Business Card for financial advisor
RVT Service Providers
Simple
Irina Lebedinskaya
Director
42 Marlow Yard
London
SW9 3QT
irina.lebedinskaya@rvtsupport.example

```html
<!DOCTYPE html>
<html lang="en">
<head>
<meta charset="utf-8">
<title>RVT Service Providers – Business Card</title>
<link href="https://fonts.googleapis.com/css2?family=Open+Sans:ital,wght@0,400;0,600;0,700;1,700&display=swap" rel="stylesheet">
<style>
  :root {
    --card-white: #ffffff;
    --brand-red: #c8161d;
    --ink-dark: #3b3b3d;
    --ink-mid: #4a4a4c;
    --band-grey: #3f3f41;
    --page-bg: #eeeeee;
  }
  html, body {
    margin: 0;
    padding: 0;
    width: 1200px;
    height: 698px;
    overflow: hidden;
    background: var(--page-bg);
  }
  .business-card {
    position: relative;
    width: 1200px;
    height: 698px;
    background: var(--card-white);
    overflow: hidden;
    font-family: "Open Sans", Arial, sans-serif;
    color: var(--ink-mid);
  }
  .brand {
    position: absolute;
    left: 82px;
    top: 140px;
    display: flex;
    align-items: center;
    gap: 26px;
  }
  .brand-square {
    width: 70px;
    height: 70px;
    background: var(--brand-red);
  }
  .brand-name {
    font-size: 82px;
    font-weight: 600;
    letter-spacing: -2px;
    color: var(--ink-dark);
    line-height: 1;
    white-space: nowrap;
  }
  .contact-list {
    position: absolute;
    left: 0;
    right: 0;
    top: 338px;
    font-size: 27px;
    color: var(--ink-mid);
  }
  .contact-row {
    display: flex;
    justify-content: center;
    align-items: center;
    gap: 44px;
    height: 52px;
    margin-left: 90px;
  }
  .contact-item {
    display: flex;
    align-items: center;
    gap: 6px;
    white-space: nowrap;
  }
  .contact-item svg {
    width: 24px;
    height: 24px;
    fill: var(--brand-red);
    flex: none;
  }
  .footer-bands {
    position: absolute;
    left: 0;
    bottom: 0;
    width: 1200px;
    height: 140px;
  }
  .footer-bands .band-grey { fill: var(--band-grey); }
  .footer-bands .band-red { fill: var(--brand-red); }
  .holder {
    position: absolute;
    right: 46px;
    bottom: 26px;
    color: var(--card-white);
    font-size: 34px;
    white-space: nowrap;
  }
  .holder-name { font-weight: 700; }
  .holder-title { font-weight: 400; font-size: 28px; }
</style>
</head>
<body>
  <main class="business-card">
    <header class="brand">
      <div class="brand-square"></div>
      <div class="brand-name">RVT Service Providers</div>
    </header>

    <section class="contact-list">
      <div class="contact-row">
        <span class="contact-item">
          <svg viewBox="0 0 24 24" aria-hidden="true"><circle cx="12" cy="12" r="11"/><path d="M8 6c1 0 1.5 2.5 1.5 3S8.5 10 8.5 10.5 10.5 14 13 15.5c.5 0 1-1 1.5-1s3 .5 3 1.5-1.5 2-2.5 2C10 18 6 13 6 8c0-1 1-2 2-2z" fill="#fff"/></svg>
          +44 (0) 203 555 0148
        </span>
        <span class="contact-item">
          <svg viewBox="0 0 24 24" aria-hidden="true"><rect x="6" y="2" width="12" height="20" rx="2"/><rect x="8" y="5" width="8" height="10" fill="#fff"/><circle cx="12" cy="18.5" r="1.3" fill="#fff"/></svg>
          +44 (0) 778 555 0193
        </span>
      </div>
      <div class="contact-row">
        <span class="contact-item">
          <svg viewBox="0 0 24 24" aria-hidden="true"><circle cx="12" cy="12" r="11"/><rect x="6" y="8" width="12" height="8" fill="#fff"/><path d="M6 8l6 4.5L18 8" stroke="#c8161d" stroke-width="1.4" fill="none"/></svg>
          irina.lebedinskaya@rvtsupport.example
        </span>
      </div>
      <div class="contact-row">
        <span class="contact-item">
          <svg viewBox="0 0 24 24" aria-hidden="true"><path d="M12 2L1 12h3v10h6v-6h4v6h6V12h3z"/></svg>
          42 Marlow Yard, London, SW9 3QT
        </span>
      </div>
    </section>

    <svg class="footer-bands" viewBox="0 0 1200 140" preserveAspectRatio="none" aria-hidden="true">
      <polygon class="band-grey" points="0,8 795,8 770,34 0,34"/>
      <polygon class="band-red" points="0,56 742,56 772,40 1200,40 1200,140 0,140"/>
    </svg>

    <div class="holder">
      <span class="holder-name">Irina Lebedinskaya,</span>
      <span class="holder-title">Director</span>
    </div>
  </main>
</body>
</html>
```